Corporate Website Homepage design

Looking for a design of a Corporate Website, Velkor Pty Ltd. Existing website is quite old, and outdated: www.velkor-example.com.au

Our company has two sides, with consumer facing brands and services for clients to develop their own brands, referred to as Private Label.

Looking for a premium design that incorporates both our services as private label and sourcing specialists, from a corporate side. And also information about our own brands, and a link to a webshop where they can be purchased.

Example General Structure:
Top Menu bar and Logo
Rotating Banner

About Our Services (well presented section of below services, with small descriptions below each one, and space to click through to learn more on each):
- Global Sourcing, Distribution & Supply Solutions
- Specialist Private Label Manufacturing Facilities
- Strict Quality Assurance Processes & Certifications

Brands:
• Pillowpop – Fun & Amazing Value range of baby Clothing, Manchester and Accessories
• Tinamorra – Luxurious Organic Baby Clothing, Wraps and Accessories
• Cradlebloom – Everything Baby at Amazing Prices
• Fenwick Tots – Infant Feeding range with all your favourite Fenwick Characters
• LinenHarbourRange – Luxury range of Towels and Manchester
• KiteTumble – Exciting range of Kids Clothing, with a twist

Product Categories:
Infant Feeding and Accessories
Infant Clothing
Infant Gear
Maternity Wear
Mens Underwear
Homewares and Manchester

Target Market(s)

Corporate Customers - Retailer buyers and Consumers looking for brand information

Industry/Entity Type

Baby

Requirements
Must have
• Good structure split by
Services, Brands and Product to allow people looking for particular things to find them quickly due to different types of visitors (corporate vs consumer)

Clean and Professional Design

with information, should have links to blog, webshop

```html
<!DOCTYPE html>
<html lang="en">
<head>
<meta charset="utf-8">
<title>Velkor Pty Ltd – Home</title>
<link href="https://fonts.googleapis.com/css2?family=Oswald:wght@400&family=Carlito:wght@400;700&family=Arimo:wght@400;700&family=Open+Sans:wght@300&display=swap" rel="stylesheet">
<style>
:root{
  --navy:#1d4f8c;
  --brand-red:#b0111c;
  --icon-blue:#1c5e9f;
  --text:#222;
  --band:#f2f2f2;
  --rule:#c4c4c4;
  --ring:#d6d6d6;
  --nav-home:#f07a1e;
  --nav-about:#3a8fd8;
  --nav-products:#9dcb2e;
  --nav-services:#b04ee0;
  --nav-brands:#ee2233;
  --nav-blog:#d8b126;
  --nav-webshop:#ff1a9c;
  --nav-contact:#16a3a5;
}
*{margin:0;padding:0;box-sizing:border-box}
html,body{width:1200px;height:2452px;overflow:hidden;background:#fff}
body{position:relative;font-family:"Arimo",Arial,sans-serif;color:var(--text)}
.abs{position:absolute}

/* header */
.site-header{position:absolute;left:0;top:0;width:1200px;height:118px;background:#fff;border-top:2px dashed #6aa6d6}
.logo{position:absolute;left:40px;top:34px;display:flex;align-items:center;gap:12px}
.logo-dot{width:30px;height:30px;border-radius:50%;background:var(--brand-red)}
.logo-name{font-family:"Carlito",sans-serif;font-weight:700;font-size:36px;color:var(--navy);letter-spacing:1px}
.main-nav{position:absolute;left:281px;top:6px;display:flex;height:106px}
.main-nav a{display:flex;align-items:center;justify-content:center;height:100%;color:#fff;text-decoration:none;font-family:"Oswald",sans-serif;font-size:25px;text-transform:uppercase;border-right:2px solid #fff;position:relative}
.nav-home{width:108px;background:var(--nav-home)}
.nav-home::after{content:"";position:absolute;bottom:-14px;left:50%;margin-left:-11px;border:11px solid transparent;border-top-color:var(--nav-home);border-top-width:0;border-bottom-color:var(--nav-home);transform:rotate(180deg);display:none}
.nav-about{width:97px;background:var(--nav-about)}
.nav-products{width:139px;background:var(--nav-products)}
.nav-services{width:122px;background:var(--nav-services)}
.nav-brands{width:115px;background:var(--nav-brands)}
.nav-blog{width:93px;background:var(--nav-blog)}
.nav-webshop{width:122px;background:var(--nav-webshop)}
.nav-contact{width:123px;background:var(--nav-contact);border-right:0}
.nav-marker{position:absolute;left:320px;top:106px;width:0;height:0;border-left:12px solid transparent;border-right:12px solid transparent;border-bottom:12px solid var(--nav-home)}

/* hero */
.hero{position:absolute;left:0;top:118px;width:1200px;height:462px;background:linear-gradient(180deg,#d9a24a 0%,#c9782a 45%,#b4561c 100%);border-bottom:5px solid var(--brand-red)}
.hero-dots{position:absolute;right:16px;bottom:16px;display:flex;gap:10px}
.hero-dots span{width:18px;height:18px;border-radius:50%;background:#fff}

/* services */
.service{position:absolute;top:628px;width:330px;text-align:center}
.service h2{font-family:"Carlito",sans-serif;font-weight:700;font-size:23px;line-height:27px;color:var(--brand-red);height:80px}
.service svg{display:block;margin:52px auto 0}
.service p{font-size:14px;line-height:17px;margin-top:22px;color:#222}
.learn-more{display:inline-block;margin-top:8px;font-size:12.5px;font-weight:700;color:#111;text-decoration:none}

/* brands */
.brands{position:absolute;left:0;top:973px;width:1200px;height:612px;background:var(--band);border-top:5px solid var(--rule);border-bottom:5px solid var(--rule)}
.brand{position:absolute;width:300px;text-align:center}
.brand-pin{position:relative;width:132px;height:150px;margin:0 auto}
.brand-pin .tail{position:absolute;left:36px;top:110px;width:0;height:0;border-left:30px solid transparent;border-right:30px solid transparent;border-top:28px solid #cfcfcf}
.brand-pin .disc{position:absolute;left:0;top:0;width:132px;height:132px;border-radius:50%;background:#fff;border:3px solid var(--ring);display:flex;align-items:center;justify-content:center;font-family:"Carlito",sans-serif;font-weight:700;font-size:18px;color:var(--navy);padding:0 8px;word-break:break-word}
.brand p{font-size:14px;line-height:17px;color:#111;margin-top:6px}

/* categories */
.categories-title{position:absolute;left:0;top:1638px;width:1200px;text-align:center;font-family:"Open Sans",sans-serif;font-weight:300;font-size:29px;color:var(--icon-blue);letter-spacing:-0.5px}
.categories-title em{font-style:normal;color:var(--brand-red)}
.category{position:absolute;width:320px;text-align:center}
.category-ring{width:190px;height:190px;margin:0 auto;border-radius:50%;border:5px solid #d8d8d8;padding:7px;background:#fff}
.category-ring .photo{width:100%;height:100%;border-radius:50%}
.category h3{font-weight:400;font-size:17px;color:#333;margin-top:26px}

/* footer */
.site-footer{position:absolute;left:0;top:2306px;width:1200px;height:146px;background:#f4f4f4;border-top:5px solid var(--rule);text-align:center}
.footer-nav{margin-top:42px;font-family:"Open Sans",sans-serif;font-weight:300;font-size:21px;color:#333}
.footer-nav a{color:#333;text-decoration:none}
.footer-nav .sep{margin:0 6px}
.copyright{font-size:12.5px;color:#333;margin-top:14px}
</style>
</head>
<body>

<header class="site-header">
  <div class="logo"><span class="logo-dot"></span><span class="logo-name">Velkor</span></div>
  <nav class="main-nav">
    <a class="nav-home" href="#">Home</a>
    <a class="nav-about" href="#">About</a>
    <a class="nav-products" href="#">Products</a>
    <a class="nav-services" href="#">Services</a>
    <a class="nav-brands" href="#">Brands</a>
    <a class="nav-blog" href="#">Blog</a>
    <a class="nav-webshop" href="#">Webshop</a>
    <a class="nav-contact" href="#">Contact</a>
  </nav>
  <span class="nav-marker"></span>
</header>

<section class="hero" role="img" aria-label="Rotating banner photo: three babies sitting among autumn leaves">
  <div class="hero-dots"><span></span><span></span><span></span></div>
</section>

<section class="services">
  <article class="service" style="left:-2px">
    <h2>Global Sourcing,<br>Distribution &amp;<br>Supply Solutions</h2>
    <svg width="68" height="68" viewBox="0 0 68 68" fill="none" stroke="var(--icon-blue)" stroke-width="3">
      <circle cx="34" cy="34" r="31"/><ellipse cx="34" cy="34" rx="14" ry="31"/>
      <line x1="3" y1="34" x2="65" y2="34"/><path d="M8 18h52M8 50h52"/><line x1="34" y1="3" x2="34" y2="65"/>
    </svg>
    <p>Lorem ipsum dolor sit amet, consectetur<br>adipisicing elit, sed do eiusmod tempor<br>incididunt ut labore et dolore magna.</p>
    <a class="learn-more" href="#">learn more &raquo;</a>
  </article>
  <article class="service" style="left:404px">
    <h2>Specialist Private<br>Label Manufacturing<br>Facilities</h2>
    <svg width="80" height="68" viewBox="0 0 80 68" fill="var(--icon-blue)">
      <g transform="translate(28 40)">
        <circle r="20"/><g><rect x="-5" y="-27" width="10" height="54"/><rect x="-5" y="-27" width="10" height="54" transform="rotate(45)"/><rect x="-5" y="-27" width="10" height="54" transform="rotate(90)"/><rect x="-5" y="-27" width="10" height="54" transform="rotate(135)"/></g>
        <circle r="8" fill="#fff"/>
      </g>
      <g transform="translate(62 18)">
        <circle r="11"/><rect x="-3.5" y="-16" width="7" height="32"/><rect x="-3.5" y="-16" width="7" height="32" transform="rotate(60)"/><rect x="-3.5" y="-16" width="7" height="32" transform="rotate(120)"/>
        <circle r="4.5" fill="#fff"/>
      </g>
    </svg>
    <p>Duis aute irure dolor in reprehenderit in voluptate<br>velit esse cillum dolore eu fugiat nulla pariatur.<br>Excepteur sint occaecat cupidatat non proident.</p>
    <a class="learn-more" href="#">learn more &raquo;</a>
  </article>
  <article class="service" style="left:821px">
    <h2>Strict Quality<br>Assurance Processes<br>&amp; Certifications</h2>
    <svg width="84" height="68" viewBox="0 0 84 68" fill="none" stroke="var(--icon-blue)" stroke-width="3">
      <rect x="3" y="5" width="78" height="52" rx="2"/><rect x="9" y="11" width="66" height="40"/>
      <path d="M40 22h28M40 30h28M40 38h20" />
      <circle cx="24" cy="30" r="9" fill="var(--icon-blue)"/><path d="M19 38l-3 22 8-5 8 5-3-22" fill="var(--icon-blue)"/>
    </svg>
    <p>Sed ut perspiciatis, unde omnis iste natus error<br>sit voluptatem accusantium doloremque<br>laudantium, totam rem aperiam eaque ipsa.</p>
    <a class="learn-more" href="#">learn more &raquo;</a>
  </article>
</section>

<section class="brands">
  <div class="brand" style="left:7px;top:63px"><div class="brand-pin"><span class="tail"></span><div class="disc">Pillowpop</div></div><p>Fun &amp; Amazing Value range of baby<br>Clothing, Manchester and Accessories</p></div>
  <div class="brand" style="left:450px;top:63px"><div class="brand-pin"><span class="tail"></span><div class="disc">Tinamorra</div></div><p>Luxurious Organic Baby Clothing,<br>Wraps and Accessories</p></div>
  <div class="brand" style="left:892px;top:63px"><div class="brand-pin"><span class="tail"></span><div class="disc">Cradlebloom</div></div><p>Everything Baby at<br>Amazing Prices</p></div>
  <div class="brand" style="left:7px;top:332px"><div class="brand-pin"><span class="tail"></span><div class="disc">Fenwick Tots</div></div><p>Infant Feeding range with all<br>your favourite Fenwick Characters</p></div>
  <div class="brand" style="left:450px;top:332px"><div class="brand-pin"><span class="tail"></span><div class="disc" style="font-size:15px">LinenHarbour Range</div></div><p>Luxury range of Towels<br>and Manchester</p></div>
  <div class="brand" style="left:892px;top:332px"><div class="brand-pin"><span class="tail"></span><div class="disc">KiteTumble</div></div><p>Exciting range of Kids<br>Clothing, with a twist</p></div>
</section>

<h2 class="categories-title">PRODUCT <em>CATEGORIES</em></h2>

<section class="category-list">
  <div class="category" style="left:8px;top:1712px"><div class="category-ring"><div class="photo" role="img" aria-label="Photo of colourful baby bottles" style="background:#b56a7a"></div></div><h3>Infant Feeding and Accessories</h3></div>
  <div class="category" style="left:440px;top:1712px"><div class="category-ring"><div class="photo" role="img" aria-label="Photo of a baby in a knitted outfit" style="background:#c9b49a"></div></div><h3>Infant Clothing</h3></div>
  <div class="category" style="left:873px;top:1712px"><div class="category-ring"><div class="photo" role="img" aria-label="Photo of a baby in a red car seat" style="background:#c0434a"></div></div><h3>Infant Gear</h3></div>
  <div class="category" style="left:8px;top:2006px"><div class="category-ring"><div class="photo" role="img" aria-label="Photo of a pregnant woman in a maternity dress" style="background:#9fb3ac"></div></div><h3>Maternity Wear</h3></div>
  <div class="category" style="left:440px;top:2006px"><div class="category-ring"><div class="photo" role="img" aria-label="Photo of men's underwear" style="background:#a88a78"></div></div><h3>Mens Underwear</h3></div>
  <div class="category" style="left:873px;top:2006px"><div class="category-ring"><div class="photo" role="img" aria-label="Photo of a furnished living room" style="background:#6e6258"></div></div><h3>Homewares and Manchester</h3></div>
</section>

<footer class="site-footer">
  <nav class="footer-nav">
    <a href="#">Home</a><span class="sep">·</span><a href="#">About</a><span class="sep">·</span><a href="#">Products</a><span class="sep">·</span><a href="#">Services</a><span class="sep">·</span><a href="#">Brands</a><span class="sep">·</span><a href="#">Blog</a><span class="sep">·</span><a href="#">Webshop</a><span class="sep">·</span><a href="#">Contact</a>
  </nav>
  <p class="copyright">Copyright @ 2010 - 2013 . All Rights Reserved</p>
</footer>

</body>
</html>
```